Meridale Freightworks Group - needs a website

Build a simple but professional website for Meridale Freightworks Group.
Web address is www.merfregro.com.au
We have just completed developing a brochure and the contents of the brochure would serve as the web pages.
Web design does not need to deviate far from the brochure and will not include electronic commerce etc at this stage.

Target Market(s)

Privately owned logistics businesses in Australia

Industry/Entity Type

Build

Number of Pages Required

5+ page

Requirements
Must have
• Professional, elegant, ability to upload video in the future, ability to add e-commerce in the future

```html
<!DOCTYPE html>
<html lang="en">
<head>
<meta charset="utf-8">
<title>MFG | Contact</title>
<link href="https://fonts.googleapis.com/css2?family=Lato:wght@300;400;700;900&display=swap" rel="stylesheet">
<style>
:root{
  --page-bg:#f1f4f8;
  --footer-bg:#e6ebf3;
  --white:#ffffff;
  --navy:#1d4f82;
  --text:#5a6470;
  --muted:#a9b3bd;
  --line:#dde3ea;
  --accent:#3d9ac6;
  --icon-grey:#c5cfd8;
  --tagline:#cfd6dd;
  --s-blue:#6ab0d6;
  --s-purple:#6f86c6;
  --s-red:#e0665d;
  --s-tan:#dfa67e;
  --s-pink:#e07fb8;
}
*{box-sizing:border-box;margin:0;padding:0}
html,body{width:1002px;height:1200px;overflow:hidden}
body{font-family:'Lato',sans-serif;background:var(--page-bg);position:relative;color:var(--text)}
.site-header{position:absolute;left:0;top:0;width:1002px;height:52px;background:var(--white);border-bottom:1px solid #e4e8ed}
.brand{position:absolute;left:16px;top:12px;font-weight:900;font-size:22px;color:var(--navy);letter-spacing:.5px}
.nav{position:absolute;top:19px;font-size:11px;letter-spacing:1.2px;color:#6b7580}
.nav-home{left:852px}
.nav-menu{left:922px}
.hero-rule{position:absolute;top:115px;height:1px;background:var(--line)}
.hero-icon{position:absolute;left:479px;top:97px}
.hero-title{position:absolute;top:162px;left:0;width:1002px;text-align:center;font-weight:300;font-size:21px;letter-spacing:2px;color:var(--navy)}
.hero-title b{font-weight:700}
.hero-intro{position:absolute;top:216px;left:0;width:1002px;text-align:center;font-size:13px;line-height:22px;font-weight:300}
.hero-intro b{font-weight:700}
.contact-panel{position:absolute;left:90px;top:310px;width:824px;height:486px;background:var(--white)}
.field{position:absolute;border:1px solid #e2e6ea;background:var(--white);font-family:'Lato',sans-serif;font-size:13px;font-weight:300;color:var(--muted);padding:0 10px;line-height:31px}
.field-message{line-height:normal;padding-top:14px}
.send-btn{position:absolute;left:192px;top:352px;width:184px;height:40px;background:var(--accent);color:var(--white);font-weight:900;font-size:11px;letter-spacing:1.3px;text-align:center;line-height:40px}
.details-title{position:absolute;left:560px;top:55px;width:210px;text-align:center;font-size:15px;font-weight:300;color:var(--navy)}
.details-title b{font-weight:700}
.detail{position:absolute;left:560px;width:210px;text-align:center;font-size:12.5px;font-weight:300;color:var(--text)}
.detail svg{display:block;margin:0 auto 6px}
.details-rule{position:absolute;left:560px;top:396px;width:212px;height:1px;background:var(--line)}
.tagline{position:absolute;top:822px;left:0;width:1002px;text-align:center;font-weight:700;font-size:29px;color:var(--tagline);letter-spacing:.3px}
.tagline .tag-brand{margin-right:28px}
.site-footer{position:absolute;left:0;top:884px;width:1002px;height:316px;background:linear-gradient(var(--footer-bg),#e4eaf3)}
.social{position:absolute;top:62px;width:36px;height:36px;border-radius:50%}
</style>
</head>
<body>
<header class="site-header">
  <div class="brand">MFG</div>
  <div class="nav nav-home">HOME</div>
  <div class="nav nav-menu">&#8964;&nbsp; MENU</div>
</header>

<div class="hero-rule" style="left:90px;width:355px"></div>
<div class="hero-rule" style="left:560px;width:354px"></div>
<svg class="hero-icon" width="45" height="36" viewBox="0 0 45 36">
  <rect x="0" y="0" width="45" height="36" rx="4" fill="var(--icon-grey)"/>
  <path d="M2 4 L22.5 19 L43 4" fill="none" stroke="var(--page-bg)" stroke-width="3"/>
</svg>
<h1 class="hero-title">CONTACT <b>MFG</b></h1>
<p class="hero-intro"><b>MFG</b> delivers <b>scale</b>, <b>synergies</b>, <b>value</b> &amp; potential <b>exit</b> to its membership.<br>To find out more and to talk directly to a representative, <b>contact us today</b>.</p>

<section class="contact-panel">
  <div class="field" style="left:51px;top:51px;width:226px;height:33px">Name</div>
  <div class="field" style="left:292px;top:51px;width:226px;height:33px">Email</div>
  <div class="field" style="left:51px;top:98px;width:467px;height:33px">Subject</div>
  <div class="field field-message" style="left:51px;top:145px;width:467px;height:178px">Message</div>
  <div class="send-btn">SEND MESSAGE</div>

  <h2 class="details-title"><b>CONTACT</b> DETAILS</h2>
  <div class="detail" style="top:94px">
    <svg width="16" height="16" viewBox="0 0 24 24"><path d="M6.6 10.8a15.1 15.1 0 0 0 6.6 6.6l2.2-2.2a1 1 0 0 1 1-.25 11.4 11.4 0 0 0 3.6.57 1 1 0 0 1 1 1V20a1 1 0 0 1-1 1A17 17 0 0 1 3 4a1 1 0 0 1 1-1h3.5a1 1 0 0 1 1 1c0 1.25.2 2.45.57 3.57a1 1 0 0 1-.25 1z" fill="var(--accent)"/></svg>
    (07) 3555 0142
  </div>
  <div class="detail" style="top:168px">
    <svg width="10" height="15" viewBox="0 0 10 15"><rect x="1" y="1" width="8" height="13" rx="1.5" fill="none" stroke="var(--accent)" stroke-width="1.6"/><rect x="4" y="11" width="2" height="1.5" fill="var(--accent)"/></svg>
    0400 555 218
  </div>
  <div class="detail" style="top:240px">
    <svg width="20" height="15" viewBox="0 0 20 15"><rect width="20" height="15" rx="1.5" fill="var(--accent)"/><path d="M1 2 L10 8.5 L19 2" fill="none" stroke="var(--white)" stroke-width="1.5"/></svg>
    ellen.marsh@merfregro.com.au
  </div>
  <div class="detail" style="top:312px">
    <svg width="21" height="18" viewBox="0 0 21 18"><rect x="1" y="1" width="19" height="12" rx="1" fill="none" stroke="var(--accent)" stroke-width="1.8"/><rect x="8" y="13" width="5" height="3" fill="var(--accent)"/><rect x="5" y="16" width="11" height="1.6" fill="var(--accent)"/></svg>
    merfregro.com.au
  </div>
  <div class="details-rule"></div>
</section>

<div class="tagline"><span class="tag-brand">MFG</span>Scale&nbsp; : &nbsp;Synergy&nbsp; : &nbsp;Value</div>

<footer class="site-footer">
  <span class="social" style="left:392px;background:var(--s-blue)"></span>
  <span class="social" style="left:437px;background:var(--s-purple)"></span>
  <span class="social" style="left:483px;background:var(--s-red)"></span>
  <span class="social" style="left:528px;background:var(--s-tan)"></span>
  <span class="social" style="left:573px;background:var(--s-pink)"></span>
</footer>
</body>
</html>
```